Criação de Power Point Slide Mestre para Planejamento de Eventos e Festas
" A empresa se posicionará como uma de grife de doces e bolos personalizados, finos e feitos à mao. Ressalto que o conceito "feito à mao" nao é apenas culinário mas também se refere a artigos de cartonagem nos quais os doces serao presenteados ou outros artigos em cartonagem que podem constar na mesa de doces, por exemplo. O Power point será utilizado para quando a cliente entrar em contato com o ateliê pedindo informaçoes sobre os doces que sao vendidos, os preços, sabores, etc. No arquivo, conterá fotos dos produtos, do que eles sao feitos e os preços, além das informaçoes sobre o ateliê, formas de pagamento, etc. O arquivo deve passar a ideia de fino e delicado. "

```html
<!DOCTYPE html>
<html lang="pt-BR">
<head>
<meta charset="UTF-8">
<title>Slide Mestre – Clara Montes</title>
<link rel="stylesheet" href="https://fonts.googleapis.com/css2?family=Cormorant+Garamond:wght@500&display=swap">
<style>
  :root {
    --page: #ffffff;
    --cocoa: #4a2411;
    --cocoa-deep: #3b1c0c;
    --cream: #e9dbc6;
    --cream-light: #efe4d3;
    --gold-dark: #b98455;
    --gold-mid: #d9ae80;
    --gold-light: #f7e6cc;
    --name-faint: #cdbba5;
  }
  html, body {
    margin: 0;
    padding: 0;
    width: 1200px;
    height: 1200px;
    overflow: hidden;
    background: var(--page);
  }
  .canvas {
    position: relative;
    width: 1200px;
    height: 1200px;
  }
  .slide {
    position: absolute;
    left: 48px;
    top: 216px;
    width: 1104px;
    height: 768px;
    overflow: hidden;
    background: radial-gradient(ellipse at 50% 50%, var(--cream-light) 0%, var(--cream) 70%);
  }
  .slide-frame {
    position: absolute;
    inset: 0;
    width: 100%;
    height: 100%;
  }
  .brand-name {
    position: absolute;
    left: 60px;
    top: 68px;
    width: 240px;
    margin: 0;
    text-align: center;
    font-family: "Cormorant Garamond", serif;
    font-weight: 500;
    font-size: 40px;
    line-height: 1;
    letter-spacing: 0.02em;
    color: var(--gold-mid);
    white-space: nowrap;
  }
  .slide-name-faint {
    position: absolute;
    left: 0;
    right: 0;
    top: 420px;
    margin: 0;
    text-align: center;
    font-family: "Cormorant Garamond", serif;
    font-weight: 500;
    font-size: 72px;
    line-height: 1;
    letter-spacing: 0.02em;
    color: var(--name-faint);
    white-space: nowrap;
  }
</style>
</head>
<body>
<div class="canvas">
  <section class="slide">
    <svg class="slide-frame" viewBox="0 0 1104 768" preserveAspectRatio="none" aria-hidden="true">
      <defs>
        <linearGradient id="ribbonGold" x1="0" y1="0" x2="1" y2="0">
          <stop offset="0" stop-color="var(--gold-dark)"/>
          <stop offset="0.45" stop-color="var(--gold-light)"/>
          <stop offset="0.75" stop-color="var(--gold-mid)"/>
          <stop offset="1" stop-color="var(--gold-light)"/>
        </linearGradient>
        <linearGradient id="lineGold" x1="0" y1="0" x2="1" y2="0">
          <stop offset="0" stop-color="var(--gold-dark)"/>
          <stop offset="0.5" stop-color="var(--gold-light)"/>
          <stop offset="1" stop-color="var(--gold-mid)"/>
        </linearGradient>
      </defs>

      <path class="band-top" fill="var(--cocoa)"
            d="M0 0 H1104 V58 C880 62 700 78 520 128 C330 182 170 212 0 206 Z"/>
      <path class="ribbon-top" fill="url(#ribbonGold)"
            d="M0 206 C170 212 330 182 520 128 C700 78 880 62 1104 58
               V70 C880 74 700 92 528 142 C340 196 170 224 0 214 Z"/>

      <path class="ribbon-bottom" fill="url(#lineGold)"
            d="M0 694 C300 698 640 686 1104 654 V662 C640 694 300 706 0 702 Z"/>
      <path class="band-bottom" fill="var(--cocoa-deep)"
            d="M0 702 C300 706 640 694 1104 662 V768 H0 Z"/>
    </svg>

    <p class="brand-name">Clara Montes</p>
    <p class="slide-name-faint">Clara Montes</p>
  </section>
</div>
</body>
</html>
```